Publisher needs book cover for search and rescue book

Book cover needed for book front sized 5.5 x 8.5 inches. About the book: The book is a technical handbook used to instruct either new search and rescue planners involved in the intelligence gathering aspect of a missing person incident or experienced providers who wish to learn new techniques and methods to collect intelligence about a missing person to better plan the field response of where to send resources or identify additional data that needs to be collected. . A background color of navy blue is preferred but open to suggestions. Interested in concepts that suggest collection of intelligence, search and rescue, law enforcement, and should be highly professional in appearance.

Target Market(s)

The target audience for the book is: Search and rescue professionals involved in the collection and analysis of intelligence used to plan where to send resources and law enforcement officers who either look for missing persons or supervise search and rescue resources.

Industry/Entity Type

Search And Rescue

Colors
0455a3

Requirements
Must have
• Title: Quiet Compass
Subtitle: Guiding the Evidence Workflow On the Hunt for Absent Travellers
The author is: Benedict R. Harlow
Image or images that brand the collection of intelligence used in search and rescue/missing persons
Nice to have
• Like the concept of an image of going deeper and deeper which each layer revealing new information.
The author has a concept of a picture that is blurry, one magnify glass reveals what the picture is, a second magnifying glass reveals even greater unexpected finding. Some designers may work with that concept, while I'm open to other designs that synthesize intelligence gathering and search and rescue/law enforcement themes.
Should not have
• No cartoons

```html
<!DOCTYPE html>
<html lang="en">
<head>
<meta charset="utf-8">
<title>Quiet Compass — Book Cover</title>
<link rel="stylesheet" href="https://fonts.googleapis.com/css2?family=Oswald:wght@300;400&family=Playfair+Display:wght@900&display=swap">
<style>
  :root {
    --backdrop: #e3ecf8;
    --navy-deep: #132c6a;
    --navy: #223f86;
    --blue-bright: #33569f;
    --blue-brand: #0455a3;
    --ink-light: #ffffff;
  }
  html, body {
    margin: 0;
    padding: 0;
    width: 1200px;
    height: 1081px;
    overflow: hidden;
    background: var(--backdrop);
  }
  .book-cover {
    position: absolute;
    left: 309px;
    top: 90px;
    width: 582px;
    height: 900px;
    overflow: hidden;
    background: var(--navy);
  }
  .cover-texture {
    position: absolute;
    inset: 0;
    width: 100%;
    height: 100%;
  }
  .cover-title {
    position: absolute;
    left: 0;
    right: 0;
    top: 26px;
    margin: 0;
    text-align: center;
    font-family: "Playfair Display", "Bodoni Moda", serif;
    font-weight: 900;
    color: var(--ink-light);
    letter-spacing: -0.03em;
    line-height: 0.92;
  }
  .cover-title .title-first {
    display: block;
    font-size: 84px;
  }
  .cover-title .title-second {
    display: block;
    font-size: 104px;
  }
  .question-mark {
    position: absolute;
    left: 0;
    right: 0;
    top: 262px;
    text-align: center;
    font-family: "Oswald", sans-serif;
    font-weight: 300;
    font-size: 270px;
    line-height: 1;
    color: rgba(255, 255, 255, 0.78);
    text-shadow: 0 0 14px rgba(255, 255, 255, 0.6), 0 0 32px rgba(180, 205, 255, 0.45);
  }
  .cover-subtitle {
    position: absolute;
    left: 0;
    right: 0;
    top: 232px;
    margin: 0;
    text-align: center;
    font-family: "Oswald", sans-serif;
    font-weight: 300;
    font-size: 56px;
    line-height: 82px;
    text-transform: uppercase;
    color: var(--ink-light);
  }
  .cover-subtitle span { display: block; }
  .cover-author {
    position: absolute;
    left: 0;
    right: 0;
    bottom: 26px;
    margin: 0;
    text-align: center;
    font-family: "Oswald", sans-serif;
    font-weight: 400;
    font-size: 26px;
    line-height: 1;
    letter-spacing: 0.18em;
    text-transform: uppercase;
    color: var(--ink-light);
  }
</style>
</head>
<body>
  <main class="book-cover">
    <svg class="cover-texture" viewBox="0 0 582 900" preserveAspectRatio="none" role="img" aria-label="Weathered, cracked navy-blue ground texture, like terrain seen under scrutiny, evoking the search for clues and intelligence">
      <defs>
        <radialGradient id="texture-glow" cx="0.5" cy="0.45" r="0.7">
          <stop offset="0" stop-color="#33569f"/>
          <stop offset="0.55" stop-color="#223f86"/>
          <stop offset="1" stop-color="#132c6a"/>
        </radialGradient>
      </defs>
      <rect width="582" height="900" fill="url(#texture-glow)"/>
    </svg>

    <h1 class="cover-title">
      <span class="title-first">Quiet</span>
      <span class="title-second">Compass</span>
    </h1>

    <div class="question-mark" aria-hidden="true">?</div>

    <p class="cover-subtitle">
      <span>Guiding</span>
      <span>The Evidence</span>
      <span>Workflow</span>
      <span>On the Hunt</span>
      <span>For</span>
      <span>Absent</span>
      <span>Travellers</span>
    </p>

    <p class="cover-author">Benedict R. Harlow</p>
  </main>
</body>
</html>
```